Business Card Design

New business card design

Target Market(s)

Residential & Commercial Property Managers

Industry/Entity Type

Plumbing Services

Contact Information for Business Card

Name - Owen Tredgold, title - Director, Phone Number - 0431 862 507, email - owen@rvb-plumbing.com.au, Company ABN - 73 215 904 386,

Font styles to use
Sans Serif

Colors
0054AA
0677BA
7BADD7
CADEEF
E8F1F8

```html
<!DOCTYPE html>
<html lang="en">
<head>
<meta charset="utf-8">
<title>RVB Plumbing Services – Business Card</title>
<link rel="stylesheet" href="https://fonts.googleapis.com/css2?family=Lato:wght@400;700;900&display=swap">
<style>
  :root {
    --stage: #a7a8ac;
    --card-light: #f4f4f4;
    --card-dark: #262d33;
    --card-dark-edge: #14191e;
    --ink: #2a2f35;
    --rule-dark: #111111;
    --rule-light: #ffffff;
    --blue-deep: #0054AA;
    --blue: #0677BA;
    --blue-soft: #7BADD7;
    --muted: #7b8087;
  }
  * { box-sizing: border-box; margin: 0; padding: 0; }
  html, body { width: 1200px; height: 960px; overflow: hidden; }
  body {
    background: radial-gradient(ellipse at 40% 45%, #c3c4c7 0%, var(--stage) 70%, #8e8f93 100%);
    font-family: "Lato", Arial, sans-serif;
    position: relative;
  }
  .card {
    position: absolute;
    left: 280px;
    width: 640px;
    height: 390px;
    border-radius: 3px;
    box-shadow: 0 14px 30px rgba(0,0,0,0.28);
    overflow: hidden;
  }
  .card--back { top: 50px; background: linear-gradient(135deg, #3a4249 0%, var(--card-dark) 45%, var(--card-dark-edge) 100%); }
  .card--front { top: 510px; background: linear-gradient(135deg, #ffffff 0%, var(--card-light) 55%, #e2e2e2 100%); }

  .brand-name {
    position: absolute;
    font-weight: 400;
    letter-spacing: 0.06em;
    white-space: nowrap;
  }
  .card--back .brand-name { color: #ffffff; left: 270px; top: 90px; font-size: 30px; }
  .card--front .brand-name { color: var(--ink); left: 170px; top: 50px; font-size: 30px; }

  .rule { position: absolute; height: 4px; }
  .card--back .rule { background: var(--rule-light); left: 0; top: 232px; width: 500px; }
  .card--back .rule-end {
    position: absolute; left: 494px; top: 226px; width: 16px; height: 16px;
    border-radius: 50%; background: var(--blue);
  }
  .card--front .rule { background: var(--rule-dark); left: 52px; top: 282px; width: 588px; height: 5px; }

  .person { position: absolute; left: 52px; top: 196px; }
  .person-name { color: var(--blue); font-weight: 900; font-size: 26px; line-height: 1.05; }
  .person-title { color: var(--ink); font-size: 17px; margin-top: 2px; }

  .contacts { position: absolute; left: 32px; top: 298px; list-style: none; }
  .contacts li { display: flex; align-items: center; gap: 10px; color: var(--ink); font-size: 19px; line-height: 30px; }
  .contacts svg { width: 16px; height: 16px; flex: none; }

  .abn {
    position: absolute; right: 30px; bottom: 24px;
    display: flex; align-items: center; gap: 10px;
    color: var(--ink); font-size: 19px;
  }
  .abn-mark { width: 14px; height: 14px; border-radius: 50%; background: var(--blue); }
</style>
</head>
<body>
  <section class="card card--back" aria-label="Business card back">
    <p class="brand-name">RVB Plumbing Services</p>
    <div class="rule"></div>
    <div class="rule-end"></div>
  </section>

  <section class="card card--front" aria-label="Business card front">
    <p class="brand-name">RVB Plumbing Services</p>
    <div class="person">
      <p class="person-name">Owen Tredgold</p>
      <p class="person-title">Director</p>
    </div>
    <div class="rule"></div>
    <ul class="contacts">
      <li>
        <svg viewBox="0 0 16 16" aria-hidden="true"><path d="M4 1.5 6.2 4 5 5.6c.8 1.9 2.2 3.4 4.1 4.3L10.6 8.7 13 11l-1.4 2.7C6.5 13.5 2.4 9.2 2.2 4z" fill="var(--blue)"/></svg>
        0431 862 507
      </li>
      <li>
        <svg viewBox="0 0 16 16" aria-hidden="true"><rect x="1" y="3" width="14" height="10" rx="1" fill="var(--blue)"/><path d="M1.5 3.5 8 9l6.5-5.5" fill="none" stroke="#ffffff" stroke-width="1.3"/></svg>
        owen@rvb-plumbing.com.au
      </li>
    </ul>
    <p class="abn">ABN - 73 215 904 386 <span class="abn-mark"></span></p>
  </section>
</body>
</html>
```